Business Consulting Company requires a website design (PSD+HTML+CSS required)

Venlora Advisory is a Business Consulting Company that provides Analysis, Business Coaching and Systems and Document Design for clients.

We would like a simplistic yet professional looking website design that uses high quality imagery to project a professional persona across our entire site.

The completed project will need to include PSD files (for editing in Photoshop) and will need to also include HTML+CSS coded files that can be edited in Adobe Dreamweaver CS5.5.

Venlora Advisory currently has a functioning website (located at www.venloraadvisory.com.au) but would like to replace its current site with something more professional, user friendly and content simplistic, with the overall design of this project being clean and very easy to navigate whilst remaining professionally focused.

A brief has been attached to this project to provide the key details but please feel free to contact me if you require any clarification or have any questions regarding the project.
Updates

Target Market(s)

The target audience for this website will be small to medium sized businesses (of all descriptions).

Industry/Entity Type

Business

Coding

Coded - Design and coding required

Number of Pages Required

5+ page

Requirements
Must have
• Simplistic design structure
• Professional images
• Easy to navigate
• Must be uploaded in PSD format
• Must be coded (HTML+CSS) and compatible with Adobe Dreamweaver CS5.5
Nice to have
• Use of the Company’s corporate colours throughout the site design
• Adding a Home page slider bar with images and short catchy messages (i.e. text based statements)
• Having a quick link box on each page that provides easy navigation throughout the site
• The use of different icons and images to depict our different services (i.e. a different icon and image for analysis service and coaching service etc.).
• All pages should follow a similar theme (universal approach to all pages)
Should not have
• When coding, images should not be used in place of text (all text must be editable)

```html
<!DOCTYPE html>
<html lang="en">
<head>
<meta charset="utf-8">
<title>Venlora Advisory</title>
<link href="https://fonts.googleapis.com/css2?family=Lato:wght@400;700&family=Roboto:wght@400;500&family=Roboto+Condensed:ital,wght@1,700&display=swap" rel="stylesheet">
<style>
:root{
  --blue:#0a9fe0;
  --footer-blue:#0499dc;
  --ink:#333;
  --muted:#777;
  --band:#f5f5f5;
  --form-band:#e3e3e3;
  --bottom:#5a5a5a;
  --dark:#2b2b2b;
}
*{box-sizing:border-box;margin:0;padding:0}
html,body{width:931px;height:1200px;overflow:hidden;background:#fff}
body{position:relative;font-family:"Roboto",Arial,sans-serif;color:var(--ink)}

/* header */
.site-header{position:absolute;left:0;top:0;width:931px;height:79px;background:linear-gradient(#fafafa,#e9ecef)}
.brand{position:absolute;left:120px;top:27px;display:flex;align-items:center;gap:8px;font-family:"Lato",sans-serif;font-size:16px;color:#666;letter-spacing:.5px;white-space:nowrap}
.brand .dot{width:26px;height:26px;border-radius:50%;background:var(--blue)}
.call-now{position:absolute;left:663px;top:13px;font-family:"Lato",sans-serif;font-size:14px;color:var(--blue);font-weight:700}
.call-now span{font-size:17px;color:#555;font-weight:400;margin-left:4px}
.main-nav{position:absolute;top:45px;left:0;font-family:"Lato",sans-serif;font-size:14px;color:#555}
.main-nav a{position:absolute;white-space:nowrap;text-decoration:none;color:inherit}
.main-nav a.active{color:var(--blue)}

/* hero */
.hero{position:absolute;left:0;top:79px;width:931px;height:281px;background:linear-gradient(100deg,#d9e1ea 0%,#a9bacb 35%,#6f88a3 62%,#8b7564 78%,#6b5443 100%)}
.hero-caption{position:absolute;left:120px;top:253px;width:391px;height:69px;background:rgba(70,70,70,.85);padding:6px 12px;font-family:"Roboto Condensed",sans-serif;font-style:italic;font-weight:700;font-size:22px;line-height:28px;color:#fff;white-space:nowrap}
.slider-tab{position:absolute;left:123px;top:338px;width:100px;height:22px;background:#f0f0f0;clip-path:polygon(12% 0,88% 0,100% 100%,0 100%)}
.slider-dot{position:absolute;top:346px;width:9px;height:9px;border-radius:50%;background:#aaa}
.slider-dot.on{background:var(--blue)}

/* services */
.service{position:absolute;top:382px;width:174px;height:190px}
.service .rule{height:2px;background:linear-gradient(90deg,#555 50%,#999 50%)}
.service .thumb{position:absolute;top:9px;left:0;width:174px;height:79px;border:1px solid #bbb}
.service h3{position:absolute;top:91px;left:0;font-family:"Lato",sans-serif;font-weight:400;font-size:12px;line-height:15px;color:#222}
.service p{position:absolute;top:127px;left:1px;width:170px;font-size:8.6px;line-height:12px;color:var(--muted)}
.service .more{position:absolute;right:0;top:175px;width:66px;height:14px;background:var(--blue);color:#fff;font-size:8px;line-height:14px;text-align:center;clip-path:polygon(16% 0,100% 0,100% 100%,0 100%)}
.service .base{position:absolute;left:0;bottom:0;width:174px;height:2px;background:var(--blue)}

/* welcome */
.welcome{position:absolute;left:0;top:593px;width:931px;height:195px;background:var(--band)}
.welcome h2{position:absolute;left:120px;top:20px;display:flex;align-items:center;gap:8px;font-family:"Lato",sans-serif;font-weight:400;font-size:31px;color:#333;white-space:nowrap}
.welcome h2 .brand-name{font-size:20px;color:#666;letter-spacing:.5px}
.welcome h2 .dot{width:26px;height:26px;border-radius:50%;background:var(--blue)}
.welcome p{position:absolute;left:120px;top:70px;width:480px;font-size:10.5px;line-height:17.4px;color:#666}
.welcome .read-more{position:absolute;left:541px;top:162px;font-size:10px;font-weight:500;color:#333}
.video{position:absolute;left:633px;top:21px;width:220px;height:151px;background:linear-gradient(#9a9a9a,#4a4a4a)}
.video .bar{position:absolute;left:0;bottom:0;width:220px;height:17px;background:#1d1d1d}
.video .play{position:absolute;left:89px;top:53px;width:40px;height:40px;border:3px solid #fff;border-radius:50%}
.video .play::after{content:"";position:absolute;left:13px;top:9px;border-left:14px solid #fff;border-top:8px solid transparent;border-bottom:8px solid transparent}

/* consultation */
.consult{position:absolute;left:0;top:788px;width:931px;height:147px;background:var(--form-band)}
.consult h2{position:absolute;left:120px;top:25px;font-family:"Lato",sans-serif;font-weight:700;font-size:18px;color:var(--blue)}
.consult .lead{position:absolute;left:120px;top:54px;width:140px;font-size:14px;line-height:20px;color:#333}
.field{position:absolute;left:291px;width:269px;height:28px;background:#fff;border-radius:3px;padding:8px 10px;font-size:11px;color:#888}
.field.details{left:583px;top:22px;height:64px}
.send{position:absolute;left:765px;top:94px;width:88px;height:30px;background:var(--blue);border-radius:3px;color:#fff;font-size:14px;font-weight:500;text-align:center;line-height:30px}

/* call band */
.call-band{position:absolute;left:0;top:935px;width:931px;height:49px;background:#f7f7f7}
.call-band .question{position:absolute;left:120px;top:14px;font-size:16px;color:#333}
.call-band .question span{font-size:19px}
.call-band .mid-dot{position:absolute;left:474px;top:16px;width:16px;height:16px;border-radius:50%;background:var(--blue)}
.call-band .touch{position:absolute;left:571px;top:15px;font-size:16.5px;color:#333}
.social-circle{position:absolute;top:13px;width:27px;height:27px;border-radius:50%;background:var(--dark);border:2px solid #bbb}

/* footer */
.site-footer{position:absolute;left:0;top:984px;width:931px;height:189px;background:var(--footer-blue);color:#fff}
.col{position:absolute;top:19px}
.col h4{font-family:"Lato",sans-serif;font-weight:400;font-size:17px;padding-bottom:6px;border-bottom:1px solid rgba(255,255,255,.55);margin-bottom:6px;white-space:nowrap}
.links li{list-style:none;font-size:10.5px;line-height:20.7px}
.newsletter p{font-size:10.5px;line-height:14px;margin-bottom:6px}
.input{width:168px;height:21px;background:#fff;color:#333;font-size:9.5px;padding:4px 6px;margin-bottom:7px}
.subscribe{display:inline-block;background:#fff;color:#333;font-size:9.5px;padding:4px 7px;border:1px solid #ccc}
.contact-row{position:relative;padding-left:22px;font-size:10.5px;line-height:14.5px;margin-bottom:4px}
.contact-row svg{position:absolute;left:0;top:1px}
.contact-row strong{font-weight:500}
.follow li{list-style:none;display:flex;align-items:center;gap:17px;font-size:10.5px;height:22px;margin-bottom:8px}
.follow .sq{width:22px;height:22px;background:#1a6fb0}
.copyright{position:absolute;left:0;top:1173px;width:931px;height:27px;background:var(--bottom);color:#eee;font-size:9.5px;text-align:center;line-height:27px}
</style>
</head>
<body>

<header class="site-header">
  <div class="brand"><span class="dot"></span>VENLORA ADVISORY</div>
  <div class="call-now">Call Us Now :<span>03 48 92 1157</span></div>
  <nav class="main-nav">
    <a class="active" style="left:380px">HOME</a>
    <a style="left:458px">ABOUT</a>
    <a style="left:542px">SERVICES</a>
    <a style="left:640px">TESTIMONIALS</a>
    <a style="left:772px">CONTACT US</a>
  </nav>
</header>

<section class="hero" role="img" aria-label="Two climbers helping each other up a rock face against a cloudy sky"></section>
<div class="hero-caption">Lorem Ipsum is simply dummy text of the<br>printing and typesetting industry.</div>
<div class="slider-tab"></div>
<span class="slider-dot on" style="left:152px"></span>
<span class="slider-dot" style="left:169px"></span>
<span class="slider-dot" style="left:186px"></span>

<article class="service" style="left:120px">
  <div class="rule"></div>
  <div class="thumb" role="img" aria-label="Consultant drawing charts on a whiteboard" style="background:linear-gradient(#f4f4f4,#cfd6dc)"></div>
  <h3>In House  Business<br>Analysis</h3>
  <p>Lorem Ipsum is simply dummy text of the printing and typesetting industry. Lorem Ipsum is simply dummy text of...</p>
  <div class="more">More</div><div class="base"></div>
</article>
<article class="service" style="left:305px">
  <div class="rule"></div>
  <div class="thumb" role="img" aria-label="Business team meeting around a table" style="background:linear-gradient(#eef0f2,#b9c2cc)"></div>
  <h3>Individual  Business<br>Coaching</h3>
  <p>Lorem Ipsum is simply dummy text of the printing and typesetting industry. Lorem Ipsum is simply dummy text of...</p>
  <div class="more">More</div><div class="base"></div>
</article>
<article class="service" style="left:492px">
  <div class="rule"></div>
  <div class="thumb" role="img" aria-label="Business process flowchart on white" style="background:linear-gradient(#ffffff,#e4efe8)"></div>
  <h3>Business System &amp;<br>Documention Creation</h3>
  <p>Lorem Ipsum is simply dummy text of the printing and typesetting industry. Lorem Ipsum is simply dummy text of...</p>
  <div class="more">More</div><div class="base"></div>
</article>
<article class="service" style="left:678px">
  <div class="rule"></div>
  <div class="thumb" role="img" aria-label="Hand writing a business plan mind map" style="background:linear-gradient(#f7f7f7,#dfe3e7)"></div>
  <h3>New Business Start Up<br>Service Packages</h3>
  <p>Lorem Ipsum is simply dummy text of the printing and typesetting industry. Lorem Ipsum is simply dummy text of...</p>
  <div class="more">More</div><div class="base"></div>
</article>

<section class="welcome">
  <h2>Welcome To <span class="dot"></span><span class="brand-name">VENLORA ADVISORY</span></h2>
  <p>Lorem Ipsum is simply dummy text of the printing and typesetting industry. Lorem Ipsum is simply dummy text of the printing and typesetting industry. Lorem Ipsum is simply dummy text of the printing and typesetting industry. Lorem Ipsum is simply dummy text of the printing and typesetting industry. Lorem Ipsum is simply dummy text of the printing and typesetting industry. Lorem Ipsum is simply dummy text of the printing and typesetting industry...</p>
  <span class="read-more">Read More.</span>
  <div class="video" role="img" aria-label="Video player showing a businessman in a suit">
    <div class="play"></div>
    <div class="bar"></div>
  </div>
</section>

<section class="consult">
  <h2>Free Consultation</h2>
  <p class="lead">Fill out the form and we will cantact you within 24 Hours:</p>
  <div class="field" style="top:22px">First Name:</div>
  <div class="field" style="top:59px">Last Name:</div>
  <div class="field" style="top:95px">Phone:</div>
  <div class="field details">Details:</div>
  <div class="send">SEND</div>
</section>

<section class="call-band">
  <p class="question">Questions? Call Us <span>(001) 555-0142</span></p>
  <span class="mid-dot"></span>
  <p class="touch">Stay in Touch:</p>
  <span class="social-circle" style="left:690px"></span>
  <span class="social-circle" style="left:723px"></span>
  <span class="social-circle" style="left:757px"></span>
  <span class="social-circle" style="left:790px"></span>
  <span class="social-circle" style="left:824px"></span>
</section>

<footer class="site-footer">
  <div class="col" style="left:120px;width:146px">
    <h4>Quick Links</h4>
    <ul class="links"><li>Home</li><li>About Us</li><li>Services</li><li>Testimonials</li><li>Contact Us</li></ul>
  </div>
  <div class="col newsletter" style="left:309px;width:166px">
    <h4>Newsletter</h4>
    <p>Signup with us and get update in your inbox.</p>
    <div class="input">Your Name</div>
    <div class="input">Email address</div>
    <span class="subscribe">SUBSCRIBE</span>
  </div>
  <div class="col" style="left:523px;width:190px">
    <h4 style="width:146px">Contact Us</h4>
    <div class="contact-row">
      <svg width="11" height="16" viewBox="0 0 11 16"><path d="M5.5 0A5.5 5.5 0 0 0 0 5.5C0 9.5 5.5 16 5.5 16S11 9.5 11 5.5A5.5 5.5 0 0 0 5.5 0z" fill="#fff"/><circle cx="5.5" cy="5.5" r="2" fill="#0499dc"/></svg>
      <strong>VENLORA ADVISORY</strong><br>Lorem ipsum dolor sit<br>amet,<br>consectetu adipiscing elit
    </div>
    <div class="contact-row">
      <svg width="9" height="14" viewBox="0 0 9 14"><rect x="0" y="0" width="9" height="14" rx="2" fill="#fff"/><rect x="2" y="2" width="5" height="8" fill="#0499dc"/></svg>
      03 48 92 1157
    </div>
    <div class="contact-row" style="margin-top:8px">
      <svg width="15" height="11" viewBox="0 0 15 11"><rect width="15" height="11" fill="#fff"/><path d="M0 0L7.5 6L15 0" stroke="#0499dc" fill="none"/></svg>
      admin@venloraadvisory.com.au
    </div>
  </div>
  <div class="col" style="left:751px;width:100px">
    <h4>Follow Us On</h4>
    <ul class="follow">
      <li><span class="sq"></span>Circlebook</li>
      <li><span class="sq"></span>Chirper</li>
      <li><span class="sq"></span>Streamview</li>
      <li><span class="sq"></span>Linkwork</li>
    </ul>
  </div>
</footer>
<div class="copyright">© 2014 VENLORA ADVISORY. ALL RIGHTS RESERVED.</div>

</body>
</html>
```